Frostwell Cool Bricks needs stationery designed for their new logo

We have a new logo so now want all our stationery to be redesigned.
Frostwell is a gel ice pack product used by the seafood & food industry to transport chilled products around the world.

We would like to use our new logo with icy or snow backgrounds or elements.
Our company tag line is "Keep your products chilled for longer"
I'll attach our old business cards so that you can use the text off them.
2nd attachment is our new logo to be used.

We want a design for:
- Business cards
- Letter Head
- Email signature

Target Market(s)

seafood & chilled food distributors

Industry/Entity Type

Industry

Font styles to use
Sans Serif

Colors
0492cd
85cae6
cee9f5

Requirements
Must have
• Our logo
Nice to have
• Snow or ice background or image incorporated somehow

```html
<!DOCTYPE html>
<html lang="en">
<head>
<meta charset="utf-8">
<title>Frostwell Stationery</title>
<link href="https://fonts.googleapis.com/css2?family=Nunito+Sans:wght@400;600;700&family=Tinos:ital@0;1&display=swap" rel="stylesheet">
<style>
:root{
  --backdrop:#444444;
  --paper:#ffffff;
  --brand-blue:#0a6fc9;
  --ice-mid:#85cae6;
  --ice-pale:#cee9f5;
  --ice-faint:#eaf5fb;
  --logo-grey:#8a8c8e;
  --ink:#222222;
  --text-grey:#444444;
  --rule:#9a9a9a;
}
*{margin:0;padding:0;box-sizing:border-box}
html,body{width:1200px;height:1200px;overflow:hidden;background:var(--backdrop)}
body{position:relative;font-family:"Nunito Sans",Arial,sans-serif;color:var(--text-grey)}
.sheet{position:absolute;background:var(--paper);overflow:hidden}
.ice{position:absolute;inset:0}
.brand{position:absolute;display:flex;align-items:center;gap:.3em;font-family:"Nunito Sans",Arial,sans-serif;font-weight:700;color:var(--logo-grey);line-height:1;white-space:nowrap}
.brand-dot{width:1.1em;height:1.1em;border-radius:50%;background:var(--brand-blue);flex:none}
.label{color:var(--brand-blue);font-weight:700;text-transform:uppercase}
.contact-icon{display:inline-block;vertical-align:middle;margin-right:.9em}

/* Letterhead */
.letterhead{left:78px;top:158px;width:581px;height:820px}
.letterhead .ice{background:
  radial-gradient(ellipse 70% 45% at 100% 100%,var(--ice-pale) 0%,rgba(206,233,245,.6) 45%,rgba(255,255,255,0) 100%),
  radial-gradient(ellipse 60% 40% at 40% 100%,var(--ice-faint) 0%,rgba(255,255,255,0) 100%)}
.letterhead .brand{left:207px;top:40px;font-size:24px}
.letter-body{position:absolute;left:73px;top:126px;width:432px;font-family:"Tinos","Times New Roman",serif;font-size:11.6px;line-height:14px;color:var(--ink);text-align:justify}
.letter-body p{margin-bottom:14px}
.letter-closing{position:absolute;left:73px;top:452px;font-family:"Tinos","Times New Roman",serif;font-size:11.6px;line-height:14px;color:var(--ink)}
.signature{position:absolute;left:73px;top:490px;width:100px;height:32px;background:linear-gradient(90deg,#e6e6e6,#f3f3f3)}
.signer{position:absolute;left:73px;top:528px;font-family:"Tinos","Times New Roman",serif;font-size:11.6px;color:var(--ink)}
.letter-footer{position:absolute;left:76px;right:0;top:764px;border-top:1px solid var(--rule);background:var(--paper);height:56px;display:flex;gap:14px;padding-top:7px;font-size:7.8px;line-height:10.5px}
.letter-footer .col{white-space:nowrap}

/* Business card front */
.card-front{left:672px;top:158px;width:298px;height:165px}
.card-front .ice{background:linear-gradient(120deg,#ffffff 0%,var(--ice-faint) 35%,var(--ice-pale) 70%,#c4e2f1 100%)}
.card-front .brand{left:20px;top:25px;font-size:16px}
.card-front .person{position:absolute;left:20px;top:98px}
.card-front .name{color:var(--brand-blue);font-weight:700;font-size:8.8px;line-height:10px}
.card-front .role{font-size:5.8px;line-height:8px}
.card-front .details{position:absolute;left:20px;right:20px;top:119px;border-top:1px solid var(--rule);padding-top:5px;display:flex;gap:8px;font-size:5.2px;line-height:8px}

/* Business card back */
.card-back{left:672px;top:336px;width:298px;height:165px}
.card-back .ice{background:
  radial-gradient(ellipse 60% 55% at 55% 50%,#f4fafd 0%,rgba(244,250,253,0) 100%),
  linear-gradient(135deg,#c6e3f2 0%,var(--ice-pale) 40%,#bddff0 75%,#a9d4ea 100%)}
.card-back .brand{left:53px;top:65px;font-size:23px}

/* Alternative card */
.card-alt{left:672px;top:514px;width:398px;height:174px}
.card-alt .brand{left:32px;top:29px;font-size:17px}
.card-alt .info{position:absolute;left:217px;top:27px;font-size:7.2px;line-height:10.2px}
.card-alt .name{color:var(--brand-blue);font-weight:700;font-size:9.8px;line-height:11px}
.card-alt .rule{width:114px;border-top:1px solid var(--rule);margin:5px 0 5px}
.card-alt .block{margin-bottom:4px}
.fan-band{position:absolute;left:0;right:0;bottom:0;height:19px;background:var(--brand-blue);display:flex;align-items:center;gap:5px;padding-left:32px;font-size:6.8px;color:#ffffff}
.fan-band .social{width:9px;height:9px;background:#ffffff;border-radius:1.5px}
.fan-band .fan-text{margin-left:6px}
</style>
</head>
<body>

<section class="sheet letterhead">
  <div class="ice" role="img" aria-label="Soft frosted ice texture fading in from the lower corner"></div>
  <div class="brand"><span class="brand-dot"></span>Frostwell</div>
  <div class="letter-body">
    <p>Gentlemen,</p>
    <p>Enclosed I have the honor to send you an article which I should be pleased if you would accept for the "Meridian Quarterly". I am <i>desperately</i> pushed for money; and in the event of Mr. Halloran's liking the "Orchard-Walk", I would take it as an especial favor if you would mail me the amount due for it, so as to reach me here by the 21st, on which day I shall need it. Can you possibly oblige me in this? If you accept the paper I presume you will allow me your usual sum, whatever that is for similar contributions—but I set no price—leaving all to your own liberality. The piece will make 8 of your pages and rather more.</p>
    <p>Will you be kind enough to put the best possible interpretation upon my behavior while in N-York? You must have conceived a <i>queer</i> idea of me—but the simple truth is that Whitcombe would insist upon <i>the juleps</i>, and I knew not what I was either doing or saying. The Review of Ashby which I offered you was deficient in a 1/2 page of commencement, which I had written to supersede the old beginning, and which gave the article the character of a general and retrospective review. No wonder you did not take it—I would have been very much mortified if you had. I hope to see you at some future time, under better auspices.</p>
  </div>
  <div class="letter-closing">In the meantime I remain<br>Yours very truly,</div>
  <div class="signature" role="img" aria-label="Handwritten signature"></div>
  <div class="signer">Elliot Marsh Vane</div>
  <footer class="letter-footer">
    <div class="col"><div class="label">Auckland</div>14 Harbour Lane, Coldwater<br>Auckland 0951</div>
    <div class="col"><div class="label">Sydney</div>57 Quay Road,<br>North Sydney, NSW 2061</div>
    <div class="col" style="padding-top:3px">
      <div><svg class="contact-icon" width="7" height="5" viewBox="0 0 7 5"><rect x=".4" y=".4" width="6.2" height="4.2" fill="none" stroke="#0a6fc9" stroke-width=".8"/><path d="M.4 .4 3.5 3 6.6 .4" fill="none" stroke="#0a6fc9" stroke-width=".8"/></svg>dana.holloway@frostwell.com.au</div>
      <div><svg class="contact-icon" width="7" height="7" viewBox="0 0 7 7"><circle cx="3.5" cy="3.5" r="3" fill="none" stroke="#0a6fc9" stroke-width=".8"/><path d="M.5 3.5h6M3.5 .5c-1.6 2-1.6 4 0 6M3.5 .5c1.6 2 1.6 4 0 6" fill="none" stroke="#0a6fc9" stroke-width=".6"/></svg>www.frostwell.com.au</div>
    </div>
  </footer>
</section>

<section class="sheet card-front">
  <div class="ice" role="img" aria-label="Frosted ice texture background"></div>
  <div class="brand"><span class="brand-dot"></span>Frostwell</div>
  <div class="person"><div class="name">Dana Holloway</div><div class="role">Business Development</div></div>
  <div class="details">
    <div><div class="label">Auckland</div>14 Harbour Lane, Coldwater<br>Auckland 0951</div>
    <div><div class="label">Sydney</div>57 Quay Road,<br>North Sydney, NSW 2061</div>
    <div style="padding-top:4px">
      <div><svg class="contact-icon" width="5" height="4" viewBox="0 0 7 5"><rect x=".4" y=".4" width="6.2" height="4.2" fill="none" stroke="#0a6fc9" stroke-width=".8"/><path d="M.4 .4 3.5 3 6.6 .4" fill="none" stroke="#0a6fc9" stroke-width=".8"/></svg>dana.holloway@frostwell.com.au</div>
      <div><svg class="contact-icon" width="5" height="5" viewBox="0 0 7 7"><circle cx="3.5" cy="3.5" r="3" fill="none" stroke="#0a6fc9" stroke-width=".8"/></svg>www.frostwell.com.au</div>
    </div>
  </div>
</section>

<section class="sheet card-back">
  <div class="ice" role="img" aria-label="Cracked blue ice texture background"></div>
  <div class="brand"><span class="brand-dot"></span>Frostwell</div>
</section>

<section class="sheet card-alt">
  <div class="brand"><span class="brand-dot"></span>Frostwell</div>
  <div class="info">
    <div class="name">Dana Holloway</div>
    <div>Business Development</div>
    <div class="rule"></div>
    <div class="block"><div class="label">Auckland</div>14 Harbour Lane, Coldwater<br>Auckland 0951</div>
    <div class="block"><div class="label">Sydney</div>57 Quay Road,<br>North Sydney, NSW 2061</div>
    <div style="margin-top:6px">
      <div><svg class="contact-icon" width="7" height="5" viewBox="0 0 7 5"><rect x=".4" y=".4" width="6.2" height="4.2" fill="none" stroke="#0a6fc9" stroke-width=".8"/><path d="M.4 .4 3.5 3 6.6 .4" fill="none" stroke="#0a6fc9" stroke-width=".8"/></svg>dana.holloway@frostwell.com.au</div>
      <div><svg class="contact-icon" width="7" height="7" viewBox="0 0 7 7"><circle cx="3.5" cy="3.5" r="3" fill="none" stroke="#0a6fc9" stroke-width=".8"/><path d="M.5 3.5h6M3.5 .5c-1.6 2-1.6 4 0 6M3.5 .5c1.6 2 1.6 4 0 6" fill="none" stroke="#0a6fc9" stroke-width=".6"/></svg>www.frostwell.com.au</div>
    </div>
  </div>
  <div class="fan-band">
    <span class="social"></span><span class="social"></span><span class="social"></span>
    <span class="fan-text">visit our fanspage on</span>
  </div>
</section>

</body>
</html>
```